Luxury Brand Coffee Table Book Template

Overview:
We are creating a premium, 28-page coffee table book to accompany every bespoke jewelry piece handcrafted by Vellmoor Jewelry. This book serves as an heirloom that documents the story, design, and craftsmanship behind each custom piece, culminating in a powerful legacy statement. We need a refined, luxurious, and masculine layout template that can be updated for each new customer.
**All reference files (images, logos, copy for pages, etc.) are included in the .zip file.
Deliverables:
Print-ready 28-page InDesign or editable template file
Front and back cover design
Consistent typography and page layouts based on our outlined structure
Design system that allows for easy photo and text updates per client
Specs:
Size: 8.1 x 10.6 in, Portrait Orientation
Cover: Black linen hardcover with gold foil stamped name or crest (simulated in mockup)
Interior: Deep matte photo paper feel – minimalistic, clean layout with generous whitespace
Color Palette: Black, white, and gold
Style: Bold, masculine, timeless, high-luxury (think Karvane Studio x Dellbrook & Co.)
See the attached 28-page outline. Please use stock image placeholders for now.
Target Market(s)
Affluent Men & Women age 35-65
Industry/Entity Type
Luxury Retail Jewelry
Font styles to use
Other font styles liked:
- I really like Trajan Pro 3, but open to suggestions, as well as a mixture of Serif and Sans Serif fonts
Look and feel
Each slider illustrates characteristics of the customer's brand and the style your logo design should communicate.

```html
<!DOCTYPE html>
<html lang="en">
<head>
<meta charset="utf-8">
<title>Vellmoor Jewelry — Heirloom Book Template</title>
<link rel="stylesheet" href="https://fonts.googleapis.com/css2?family=Cinzel:wght@600&family=Playfair+Display:wght@700&family=Tinos:wght@400;700&display=swap">
<style>
  :root {
    --black: #000000;
    --white: #ffffff;
    --paper: #ffffff;
    --gold: #e3a93e;
    --gold-band: #f3b451;
    --foil: #c99a3a;
    --ink: #111111;
    --rule: #8a8a8a;
  }
  * { margin: 0; padding: 0; box-sizing: border-box; }
  html, body { width: 1200px; height: 1200px; overflow: hidden; background: var(--paper); }
  body { position: relative; font-family: "Tinos", "Times New Roman", serif; color: var(--ink); }

  .page { position: absolute; overflow: hidden; }
  .cover { left: 22px; top: 375px; width: 342px; height: 450px; background: var(--black); }
  .page--final  { left: 389px; top: 79px;  width: 376px; height: 494px; background: var(--black); }
  .page--story  { left: 786px; top: 79px;  width: 376px; height: 494px; background: var(--white); }
  .page--sketch { left: 389px; top: 627px; width: 376px; height: 494px; background: var(--white); }
  .page--design { left: 786px; top: 627px; width: 376px; height: 494px; background: var(--black); color: var(--white); }

  /* cover */
  .cover__brand { position: absolute; left: 0; right: 0; top: 215px; display: flex; justify-content: center; align-items: center; gap: 6px; }
  .cover__dot { width: 20px; height: 20px; border: 1.5px solid var(--foil); border-radius: 50%; }
  .cover__name { font-family: "Cinzel", "Times New Roman", serif; font-weight: 600; font-size: 11px; letter-spacing: 0.5px; color: var(--foil); }

  /* page 1 */
  .photo-ring { position: absolute; inset: 0;
    background: linear-gradient(160deg, #2a2410 0%, #6e6430 30%, #8a5a44 50%, #4a4320 72%, #121008 100%); }
  .tab { position: absolute; left: 352px; top: 203px; width: 24px; height: 88px; background: var(--gold-band); }

  .folio { position: absolute; top: 479px; font-size: 5.6px; letter-spacing: 0.2px; }
  .folio--left { left: 12px; }
  .folio--right { right: 12px; }
  .folio--light { color: var(--white); }

  /* page 2 */
  .spine-strip { position: absolute; left: 0; top: 0; width: 88px; height: 100%; background: var(--black); }
  .band { position: absolute; left: 0; top: 203px; width: 100%; height: 88px; background: var(--gold-band); }
  .band__title { position: absolute; left: 42px; top: 0; height: 88px; line-height: 88px; font-family: "Playfair Display", serif; font-weight: 700; font-size: 84px; letter-spacing: 2px; color: var(--black); }

  .heading { font-weight: 700; font-size: 10px; letter-spacing: 0.4px; text-transform: uppercase; }
  .body { font-size: 6.9px; line-height: 9.3px; text-align: justify; }

  .story__head { position: absolute; left: 102px; top: 30px; }
  .story__col { position: absolute; top: 54px; width: 122px; }
  .story__col--a { left: 102px; }
  .story__col--b { left: 242px; }
  .note__head { position: absolute; left: 102px; top: 308px; }
  .note__body { position: absolute; left: 102px; top: 329px; width: 262px; }

  /* page 3 */
  .sketch { position: absolute; left: 52px; top: 16px; width: 222px; height: 456px;
    background: linear-gradient(180deg, #d9a54a 0%, #b87a2c 50%, #d9a54a 100%); }
  .side-strip { position: absolute; left: 321px; top: 0; width: 55px; height: 100%; background: var(--black); }
  .side-strip__line { position: absolute; top: 0; width: 1px; background: var(--white); }
  .side-strip__line--a { left: 8px; height: 400px; }
  .side-strip__line--b { left: 18px; height: 364px; }

  /* page 4 */
  .design__title { position: absolute; left: 12px; top: 12px; font-family: "Playfair Display", serif; font-weight: 700; font-size: 80px; letter-spacing: 7px; line-height: 1; color: var(--white); }
  .design__rule { position: absolute; left: 146px; top: 95px; width: 230px; height: 1px; background: var(--rule); }
  .design__head { position: absolute; color: var(--gold); }
  .design__body { position: absolute; width: 158px; }
  .design__head--origin { left: 20px; top: 126px; }
  .design__body--origin { left: 20px; top: 148px; }
  .design__head--inspiration { left: 200px; top: 126px; }
  .design__body--inspiration { left: 200px; top: 148px; }
  .design__head--symbols { left: 20px; top: 283px; }
  .design__body--symbols { left: 20px; top: 305px; }
  .emblem { position: absolute; left: 196px; top: 273px; width: 160px; height: 164px;
    background: linear-gradient(180deg, #d9a54a 0%, #a8701f 100%); }
</style>
</head>
<body>

<section class="page cover" aria-label="Front cover">
  <div class="cover__brand">
    <span class="cover__dot"></span>
    <span class="cover__name">Vellmoor Jewelry</span>
  </div>
</section>

<section class="page page--final" aria-label="Page 1, final piece">
  <div class="photo-ring" role="img" aria-label="Photograph of the finished signet ring on black with its reflection"></div>
  <div class="tab"></div>
  <p class="folio folio--left folio--light">Page 1 | FINAL PIECE</p>
</section>

<section class="page page--story" aria-label="Page 2, story">
  <div class="spine-strip"></div>
  <h2 class="heading story__head">Customer’s Story</h2>
  <p class="body story__col story__col--a">noximih icatressati, duciae hin de fat potatisser lostortum pere, spio, viliac vivil terei in tam sa vessidiem vit, foremus effre ala egita ommolib ussere dum re, fuidenatus Ad iam consula dereisquam sulemuri sin se noviteribus. Valiberei si teris bonsis inate diti tam pes iamquemus haberum, quam dius, veris inati, tam nons patiem non deribunum numenih ilicesse, conontella ca; nunum nondio, nonos, cessessatore esse vicis. Raverem. Graces num non sultora volicul lericienatam moressunte fu</p>
  <p class="body story__col story__col--b">Ilicepop ublicerei perdie egere noximih icatressati, duciae hin de fat potatisser lostortum pere, spio, viliac vivil terei in tam sa vessidiem vit, foremus effre ala egita ommolib ussere dum re, fuidenatus Ad iam consula dereisquam sulemuri sin se noviteribus. Valiberei si teris bonsis inate diti tam pes iamquemus haberum, quam dius, veris inati, tam nons patiem non deribunum numenih ilicesse, conontella ca; nunum nondio, nonos, cessessatore esse vicis.</p>
  <div class="band"><h1 class="band__title">STORY</h1></div>
  <h2 class="heading note__head">Note from the Designer</h2>
  <p class="body note__body">Ilicepop ublicerei perdie egere noximih icatressati, duciae hin de fat potatisser lostortum pere, spio, viliac vivil terei in tam sa vessidiem vit, foremus effre ala egita ommolib ussere dum re, fuidenatus Ad iam consula dereisquam sulemuri sin se noviteribus. Valiberei si teris bonsis inate diti tam pes iamquemus haberum, quam dius, veris inati, tam nons patiem non deribunum numenih ilicesse, conontella ca; nunum nondio, nonos, cessessatore esse vicis.</p>
  <p class="folio folio--right">STORY | Page 2</p>
</section>

<section class="page page--sketch" aria-label="Page 3, initial design sketch">
  <div class="sketch" role="img" aria-label="Initial crest design sketch for the ring"></div>
  <div class="side-strip">
    <span class="side-strip__line side-strip__line--a"></span>
    <span class="side-strip__line side-strip__line--b"></span>
  </div>
  <p class="folio folio--left">Page 3 | INITIAL DESIGN SKETCH</p>
</section>

<section class="page page--design" aria-label="Page 4, design">
  <h1 class="design__title">DESIGN</h1>
  <div class="design__rule"></div>
  <h2 class="heading design__head design__head--origin">Origin of the Concept</h2>
  <p class="body design__body design__body--origin">noximih icatressati, duciae hin de fat potatisser lostortum pere, spio, viliac vivil terei in tam sa vessidiem vit, foremus effre ala egita ommolib ussere dum re, fuidenatus Ad iam consula dereisquam sulemuri sin se noviteribus. Valiberei si teris bonsis inate diti tam pes iamquemus haberum, quam dius, veris inati, tam nons patiem non deribunum numenih ilicesse, conontella ca; nunum nondio, nonos, cessessatore esse vicis. Raverem. Graces num non sultora volicul lericienatam moressunte fu</p>
  <h2 class="heading design__head design__head--inspiration">Inspiration</h2>
  <p class="body design__body design__body--inspiration">noximih icatressati, duciae hin de fat potatisser lostortum pere, spio, viliac vivil terei in tam sa vessidiem vit, foremus effre ala egita ommolib ussere dum re, fuidenatus Ad iam consula dereisquam sulemuri sin se noviteribus. Valiberei si teris bonsis inate diti tam pes iamquemus haberum, quam dius, veris inati, tam nons patiem non deribunum numenih ilicesse, conontella ca; nunum nondio, nonos, cessessatore esse vicis. Raverem. Graces num non sultora volicul lericienatam moressunte fu</p>
  <h2 class="heading design__head design__head--symbols">Symbolisms</h2>
  <p class="body design__body design__body--symbols">noximih icatressati, duciae hin de fat potatisser lostortum pere, spio, viliac vivil terei in tam sa vessidiem vit, foremus effre ala egita ommolib ussere dum re, fuidenatus Ad iam consula dereisquam sulemuri sin se noviteribus. Valiberei si teris bonsis inate diti tam pes iamquemus haberum, quam dius, veris inati, tam nons patiem non deribunum numenih ilicesse, conontella ca; nunum nondio, nonos, cessessatore esse vicis. Raverem. Graces num non sultora volicul lericienatam moressunte fu</p>
  <div class="emblem" role="img" aria-label="Gold heraldic emblem illustration"></div>
  <p class="folio folio--right folio--light">DESIGN | Page 4</p>
</section>

</body>
</html>
```